Label design for an exciting new Vodka brand

We need a label design for a dynamic new Vodka brand called 'Pale lantern Vodka'. It is a crisp and versatile liquid with a clean and smooth finish. It should appeal to 21-39 year olds, with a slight female skew. Colours, fonts and styles should be modern and relatively neutral - take inspiration from the brand pictures attached.

Target Market(s)

21-39 year olds, both male and female, but with a slight female skew

```html
<!DOCTYPE html>
<html lang="en">
<head>
<meta charset="utf-8">
<title>Pale lantern Vodka – Label</title>
<link href="https://fonts.googleapis.com/css2?family=Great+Vibes&family=Montserrat:wght@500;600&family=Encode+Sans+Condensed:wght@300;400&display=swap" rel="stylesheet">
<style>
  :root {
    --backdrop: #eef0f3;
    --label-white: #ffffff;
    --blue-light: #c9d7e4;
    --blue-mid: #98b1c7;
    --blue-deep: #7895b0;
    --script-white: #ffffff;
    --ink-dark: #2b2b2b;
    --ink-grey: #6a6a6a;
    --tagline-blue: #9db3c8;
    --rule: #8a8a8a;
  }
  * { margin: 0; padding: 0; box-sizing: border-box; }
  html, body {
    width: 1200px; height: 1200px; overflow: hidden;
    background: var(--backdrop);
  }
  .label {
    position: absolute; left: 260px; top: 80px;
    width: 680px; height: 1040px;
    background: var(--label-white);
    box-shadow: 0 4px 24px rgba(60, 80, 100, 0.12);
    overflow: hidden;
  }
  .label__panel {
    position: absolute; left: 0; top: 0; width: 100%; height: 755px;
    background: linear-gradient(105deg, var(--blue-light) 0%, var(--blue-mid) 30%, var(--blue-deep) 55%, var(--blue-mid) 85%, var(--blue-light) 100%);
  }
  .brand-script {
    position: absolute; left: 48px; top: 395px;
    font-family: "Great Vibes", cursive;
    font-size: 118px; line-height: 1;
    color: var(--script-white);
  }
  .brand-name {
    position: absolute; left: 0; right: 0; top: 548px;
    text-align: center;
    font-family: "Montserrat", sans-serif;
    font-weight: 600; font-size: 112px; line-height: 1;
    letter-spacing: 2px;
    color: var(--script-white);
  }
  .label__base {
    position: absolute; left: 0; top: 755px; width: 100%; height: 285px;
    text-align: center;
  }
  .spirit {
    position: absolute; left: 0; right: 0; top: 42px;
    font-family: "Montserrat", sans-serif;
    font-weight: 600; font-size: 78px; line-height: 1;
    letter-spacing: 9px;
    color: var(--ink-dark);
  }
  .tagline {
    position: absolute; left: 0; right: 0; top: 130px;
    font-family: "Encode Sans Condensed", sans-serif;
    font-weight: 400; font-size: 24px; letter-spacing: 2px;
    color: var(--tagline-blue);
  }
  .details {
    position: absolute; left: 42px; right: 42px; top: 180px;
    border-top: 1px solid var(--rule);
    display: flex; justify-content: space-between; align-items: center;
    padding-top: 10px;
    font-family: "Encode Sans Condensed", sans-serif;
    font-weight: 300; font-size: 22px;
    color: var(--ink-grey);
  }
  .details__sep {
    width: 1px; height: 46px; background: var(--rule);
  }
  .details__item--wide { word-spacing: 6px; }
</style>
</head>
<body>
  <div class="label">
    <div class="label__panel">
      <div class="brand-script">Pale</div>
      <div class="brand-name">LANTERN</div>
    </div>
    <div class="label__base">
      <div class="spirit">VODKA</div>
      <div class="tagline">CLEAN AND SMOOTH FINISH</div>
      <div class="details">
        <span class="details__item">NET.WT.750 ML</span>
        <span class="details__sep"></span>
        <span class="details__item details__item--wide">SMALL BATCH &nbsp;HAND CRAFTED</span>
        <span class="details__sep"></span>
        <span class="details__item">40% ALC/VOL</span>
      </div>
    </div>
  </div>
</body>
</html>
```